Geschäftspapiere für Softwareentwicklung/Consulting
Zielgruppe
Wir sind in der Softwareentwicklung / Consulting tätig und unterstützen durch externe Mitarbeit große und mittelständige Unternehmen.
Aufgabenstellung
Die Farben unseres Logos sollen aufgenommen werden. Der rechte Rand soll Angaben wie, Anschrift, Bankverbindung und Geschäftsdaten beinhalten - diese sollen nicht im Footer erscheinen. Das ganze sollte nicht zu bunt gestaltet werden.

```html
<!DOCTYPE html>
<html lang="de">
<head>
<meta charset="utf-8">
<title>fernbyte – Geschäftspapiere</title>
<link href="https://fonts.googleapis.com/css2?family=Open+Sans:wght@400;600;700&family=Arimo:wght@400;700&display=swap" rel="stylesheet">
<style>
:root{
  --backdrop:#cdcdcd;
  --paper:#ffffff;
  --ink:#4a4a4a;
  --ink-soft:#6b6b6b;
  --brand-blue:#1e9bd7;
  --brand-teal:#1aa68a;
  --window:#4d4d4d;
  --rule:#b5b5b5;
  --shadow:0 3px 8px rgba(0,0,0,.35);
}
*{margin:0;padding:0;box-sizing:border-box}
html,body{width:1200px;height:1200px;overflow:hidden;background:var(--backdrop)}
body{position:relative;font-family:"Open Sans",sans-serif;color:var(--ink)}
.sheet{position:absolute;background:var(--paper);box-shadow:var(--shadow)}
.brand-name{font-family:"Open Sans",sans-serif;font-weight:600;color:var(--ink);letter-spacing:.2px;white-space:nowrap}

/* envelope back */
.envelope-back{left:44px;top:68px;width:528px;height:264px;box-shadow:none}
.envelope-back svg.flap{position:absolute;left:0;top:0}
.envelope-back .brand-name{position:absolute;left:0;width:528px;top:30px;text-align:center;font-size:16px}

/* envelope front */
.envelope-front{left:628px;top:68px;width:528px;height:264px}
.envelope-front .brand-name{position:absolute;left:60px;top:38px;font-size:26px}
.address-window{position:absolute;left:53px;top:121px;width:218px;height:109px;border-radius:15px;background:var(--window)}
.return-address{position:absolute;right:30px;top:209px;text-align:right;font-size:6.6px;line-height:8.6px;letter-spacing:.3px}
.return-address strong{color:var(--brand-blue);font-weight:700}

/* letterhead */
.letter{left:40px;top:440px;width:504px;height:713px}
.letter-second{left:640px;top:440px;width:504px;height:713px}
.letter .brand-name{position:absolute;left:52px;top:40px;font-size:25px}
.letter-second .brand-name{position:absolute;right:38px;top:38px;font-size:11px}
.sidebar{position:absolute;right:34px;top:29px;text-align:right;font-size:5.4px;line-height:7.6px;padding-right:8px;border-right:2.5px solid var(--rule);height:110px}
.sidebar strong{color:var(--brand-blue);font-weight:700}
.sidebar .label{color:var(--brand-blue);display:inline-block;width:22px;text-align:left}
.sidebar .gap{height:5px}
.address-field{position:absolute;left:51px;top:107px;width:205px;height:99px}
.address-field svg{position:absolute;left:0;top:0}
.sender-line{position:absolute;left:13px;top:6px;font-size:4.6px;white-space:nowrap}
.sender-line strong{color:var(--brand-blue);font-weight:600}
.sender-line .sep{color:var(--brand-blue)}
.recipient{position:absolute;left:87px;top:148px;font-family:"Arimo",sans-serif;font-size:6.4px;line-height:11.8px}
.date{position:absolute;left:80px;top:231px;font-family:"Arimo",sans-serif;font-size:8px}
.fold-mark{position:absolute;left:2px;width:13px;height:1px;background:var(--ink)}
.body-copy{position:absolute;left:51px;top:270px;width:407px;font-family:"Arimo",sans-serif;font-size:6.3px;line-height:13.6px;text-align:justify;color:var(--ink-soft)}
.body-copy p+p{margin-top:13.6px;text-align:left}
.closing{position:absolute;left:337px;top:568px;font-family:"Arimo",sans-serif;font-weight:700;font-size:9.4px;color:#111}
.signature{position:absolute;left:305px;top:572px;width:130px;height:109px;background:linear-gradient(135deg,rgba(30,120,200,.12),rgba(30,120,200,.22));border-radius:4px}
.footer-bar{position:absolute;left:35px;top:692px;width:433px;height:5px;background:var(--rule)}
</style>
</head>
<body>

<section class="sheet envelope-back">
  <svg class="flap" width="528" height="264" viewBox="0 0 528 264" aria-hidden="true">
    <rect width="528" height="264" fill="#fff"/>
    <path d="M0 0 L528 0 L502 65 Q497 75 485 75 L43 75 Q31 75 26 65 Z" fill="#fff" stroke="#e4e4e4" stroke-width="1.2"/>
  </svg>
  <span class="brand-name">fernbyte</span>
</section>

<section class="sheet envelope-front">
  <span class="brand-name">fernbyte</span>
  <div class="address-window"></div>
  <address class="return-address" style="font-style:normal">
    <strong>fernbyte GmbH</strong><br>
    Lindenhofweg 12<br>
    63128 Heusenfeld, Germany
  </address>
</section>

<section class="sheet letter">
  <span class="brand-name">fernbyte</span>
  <aside class="sidebar">
    <strong>fernbyte GmbH</strong><br>
    Lindenhofweg 12<br>
    63128 Heusenfeld, Germany
    <div class="gap"></div>
    <span class="label">Tel.:</span>+49 6100 5550123<br>
    <span class="label">Mail:</span>mork@fernbyte-it.de<br>
    <span class="label">Web:</span>www.fernbyte-it.de
    <div class="gap"></div>
    Kelstadt HRB 4410 KS<br>
    Steuer Nr. 00 111 22233<br>
    Nordtal Bank Kelstadt<br>
    DE00 1234 0000 XXXX 0000 00<br>
    NOTADEXXXXXXXXX
  </aside>

  <div class="address-field">
    <svg width="205" height="99" viewBox="0 0 205 99" aria-hidden="true" fill="none" stroke="#555" stroke-width=".8">
      <path d="M0.5 17 V9 Q0.5 0.5 9 0.5 H17"/>
      <path d="M188 0.5 H196 Q204.5 0.5 204.5 9 V17"/>
      <path d="M0.5 82 V90 Q0.5 98.5 9 98.5 H17"/>
      <path d="M188 98.5 H196 Q204.5 98.5 204.5 90 V82"/>
    </svg>
    <div class="sender-line"><strong>fernbyte GmbH</strong>&nbsp; Lindenhofweg 12 <span class="sep">|</span> 63128 Heusenfeld <span class="sep">|</span> Germany</div>
  </div>

  <div class="recipient">Marlene Voss<br>Am Birkenhang 8<br>53700 Talbrück<br>SCHWEIZ</div>
  <div class="date">25 März 2021</div>

  <span class="fold-mark" style="top:251px"></span>
  <span class="fold-mark" style="top:506px"></span>

  <div class="body-copy">
    <p>Lorem ipsum dolor sit amet, consectetur adipiscing elit. Vestibulum adipiscing felis ac tortor consectetur feugiat. Etiam malesuada sodales eros ut ornare. Sed lorem eros, mattis id pretium ut, faucibus sit amet quam. Nullam consectetur ultricies ipsum, fringilla porttitor erat ornare at. Sed sit amet dui vel sapien ultrices vulputate. In hac habitasse platea dictumst. Nam est nisi, rhoncus at sagittis a, porttitor adipiscing nulla. Vivamus placerat felis ultrices quam iaculis eget dignissim felis egestas. Integer nec molestie lorem. Sed odio tellus, vulputate sed laoreet non, vulputate id justo. Etiam suscipit, odio vel auctor dictum, felis turpis ullamcorper neque, quis sodales risus metus in magna. Morbi pellentesque justo et quam laoreet facilisis. Aenean placerat, urna ornare aliquet tincidunt, lorem justo molestie ligula, id placerat est metus nec lectus. Nullam eu ipsum quis turpis tristique iaculis rutrum nec nibh. Phasellus risus eros, semper sit amet faucibus sit amet, laoreet et neque. Donec eros sem, viverra dictum faucibus quis, ullamcorper tincidunt nulla.</p>
    <p>Aenean ut congue tellus. Class aptent taciti sociosqu ad litora torquent per conubia nostra, per inceptos himenaeos. Sed facilisis, velit tincidunt pharetra fermentum, urna tortor iaculis erat, vitae sollicitudin leo mauris quis mi. Cras malesuada sem ac ipsum sagittis ultrices. Mauris fermentum porttitor nisi, eu facilisis lorem consectetur et. Suspendisse est elit, scelerisque ac euismod id, scelerisque viverra odio. Nullam scelerisque metus in eros semper congue. Fusce a fermentum est. Ut ac leo dolor. Quisque dignissim mauris a neque luctus pretium ultrices risus sagittis. Aenean quam massa, rutrum ac hendrerit eu, interdum eu nulla. Curabitur a velit mauris, sed porta eros. Cras id egestas sapien. Proin non metus eget felis eleifend adipiscing. Nunc malesuada pharetra blandit.</p>
  </div>

  <div class="signature" role="img" aria-label="Handwritten signature in blue ink"></div>
  <div class="closing">Your sincerely</div>
  <div class="footer-bar"></div>
</section>

<section class="sheet letter-second">
  <span class="brand-name">fernbyte</span>
  <span class="fold-mark" style="top:251px"></span>
  <span class="fold-mark" style="top:506px"></span>
</section>

</body>
</html>
```